photowall advertisement

We require a wall featuring our company logo. We would like to avoid the color green, and gold is highly preferred. The design should be similar to the one in the attached photo. The wall will be used for photos and promotional purposes during congresses. Files must be prepared for printing.
dimension of wall: 470x223 cm

Industry/Entity Type

lifestyle

Colors
0054AA
0677BA
7BADD7
CADEEF
E8F1F8
6B429C
8869AF
B7A5CE
E3DAEB
F3F0F8

Requirements
Must have
• gold color, white, and other compare with gold color
Nice to have
• some pictograms, maps of Europe

```html
<!DOCTYPE html>
<html lang="en">
<head>
<meta charset="utf-8">
<title>Novaline Technology – Photo Wall</title>
<link rel="stylesheet" href="https://fonts.googleapis.com/css2?family=Michroma&family=Montserrat:wght@300&display=swap">
<style>
  :root {
    --stage: #6f6f6f;
    --wall: #ffffff;
    --gold: #f5b00f;
    --gold-soft: #f6ae52;
    --gold-pale: #f8e2b4;
    --ink: #1d1a1a;
    --sand: #ddd2bd;
  }
  html, body {
    margin: 0;
    padding: 0;
    width: 1008px;
    height: 1200px;
    overflow: hidden;
    background: var(--stage);
  }
  .photo-wall {
    position: absolute;
    left: 24px;
    top: 372px;
    width: 960px;
    height: 455px;
    background: var(--wall);
    overflow: hidden;
  }
  .photo-wall svg { display: block; width: 100%; height: 100%; }
  .brand-name {
    font-family: "Michroma", sans-serif;
    font-size: 58px;
    fill: var(--ink);
    letter-spacing: 4px;
  }
  .brand-tagline {
    font-family: "Montserrat", sans-serif;
    font-weight: 300;
    font-size: 22px;
    letter-spacing: 14px;
    fill: var(--ink);
  }
  .decor { opacity: 0.9; }
</style>
</head>
<body>
<main class="photo-wall">
  <svg viewBox="0 0 1414 670" xmlns="http://www.w3.org/2000/svg" aria-labelledby="wall-title">
    <title id="wall-title">Novaline Technology photo wall</title>
    <defs>
      <linearGradient id="pattern-tone" x1="0" y1="0" x2="1" y2="1">
        <stop offset="0" stop-color="#f5b00f"/>
        <stop offset="0.55" stop-color="#e9d6a6"/>
        <stop offset="1" stop-color="#3b3331"/>
      </linearGradient>
      <radialGradient id="map-tone" cx="0.55" cy="0.45" r="0.6">
        <stop offset="0" stop-color="#dccfb6"/>
        <stop offset="1" stop-color="#ebe3d3"/>
      </radialGradient>
      <linearGradient id="icon-tone" x1="0" y1="0" x2="1" y2="1">
        <stop offset="0" stop-color="#f8d48a"/>
        <stop offset="1" stop-color="#f6ae52"/>
      </linearGradient>
    </defs>

    <!-- map area -->
    <rect class="europe-map" role="img" aria-label="Dotted map of Europe in sand tones"
          x="390" y="110" width="570" height="460" rx="60" fill="url(#map-tone)" opacity="0.85"/>

    <!-- corner pattern areas -->
    <rect class="corner-pattern corner-pattern--top-left" role="img" aria-label="Gold and charcoal concentric arc tiles"
          x="0" y="0" width="290" height="290" fill="url(#pattern-tone)"/>
    <rect class="corner-pattern corner-pattern--bottom-right" role="img" aria-label="Gold and charcoal concentric arc tiles"
          x="1125" y="372" width="289" height="298" fill="url(#pattern-tone)"/>

    <!-- decorative tech pictograms, shown as soft tone areas -->
    <rect class="decor" role="img" aria-label="Gold half-circle and bowl pictogram" x="378" y="30" width="136" height="110" rx="14" fill="url(#icon-tone)"/>
    <rect class="decor" role="img" aria-label="USB stick pictogram" x="690" y="40" width="80" height="60" rx="14" fill="url(#icon-tone)"/>
    <rect class="decor" role="img" aria-label="Laptop with play button pictogram" x="1082" y="100" width="200" height="150" rx="14" fill="url(#icon-tone)"/>
    <rect class="decor" role="img" aria-label="Processor chip pictogram" x="1126" y="300" width="96" height="96" rx="14" fill="url(#icon-tone)"/>
    <rect class="decor" role="img" aria-label="Code tag pictogram" x="206" y="282" width="64" height="34" rx="10" fill="url(#icon-tone)"/>
    <rect class="decor" role="img" aria-label="Dashed zigzag lines" x="0" y="380" width="112" height="100" rx="14" fill="url(#icon-tone)" opacity="0.6"/>
    <rect class="decor" role="img" aria-label="Cloud sync pictogram" x="192" y="450" width="112" height="80" rx="14" fill="url(#icon-tone)"/>
    <rect class="decor" role="img" aria-label="Gold chevron frame" x="0" y="530" width="64" height="125" rx="10" fill="url(#icon-tone)"/>
    <rect class="decor" role="img" aria-label="Framed square pictogram" x="452" y="582" width="72" height="72" rx="10" fill="url(#icon-tone)"/>
    <rect class="decor" role="img" aria-label="Gold and black plus pictogram" x="898" y="572" width="104" height="98" rx="12" fill="url(#icon-tone)"/>

    <!-- simple common icons -->
    <g class="icon-share" fill="var(--ink)" stroke="var(--ink)" stroke-width="4">
      <line x1="104" y1="584" x2="150" y2="560"/>
      <line x1="104" y1="584" x2="150" y2="610"/>
      <circle cx="104" cy="584" r="9"/><circle cx="150" cy="558" r="9"/><circle cx="150" cy="612" r="9"/>
    </g>
    <g class="icon-cross" stroke="var(--ink)" stroke-width="7" stroke-linecap="round">
      <path d="M965 125 L985 145 M985 125 L965 145"/>
      <path d="M1077 468 L1097 488 M1097 468 L1077 488"/>
    </g>
    <path class="edge-half-disc" d="M1414 195 A75 75 0 0 0 1414 345 Z" fill="var(--gold)"/>

    <!-- brand -->
    <g class="brand">
      <rect class="brand-mark" x="382" y="304" width="70" height="70" fill="var(--ink)"/>
      <text class="brand-name" x="474" y="358">NOVALINE</text>
      <text class="brand-tagline" x="612" y="400">TECHNOLOGY</text>
    </g>
  </svg>
</main>
</body>
</html>
```